" LUMIVEX Somos uma Autoridade de Registro (AR) com autorização de funcionamento concedida pelo Governo Federal, responsável pelo recebimento, validação, encaminhamento de solicitações de emissão ou revogação de certificados digitais e identificação, de forma presencial, de seus solicitantes. Estamos entre as melhores do Brasil, fornecendo Certificados Digitais (cuja definição encontra-se em http://www.oquarel.org.br/certificacao-digital/o-que-e), além de projetos especiais, para garantir a autenticidade, a integridade e a validade jurídica de documentos em forma eletrônica, das aplicações de suporte e das aplicações habilitadas que utilizem certificados digitais, bem como a realização de transações eletrônicas seguras, através de nossos Pontos de Atendimentos com abrangência nacional. Os benefícios dos Certificados Digitais e onde usá-los: http://www.oquarel.org.br/certificacao-digital/beneficios A Lumivex atuando no mercado de identificação digital disponibiliza a seus clientes a nova geração de certificados digitais. São inovadores, simples, rápidos, confiáveis, seguros, práticos, e, sobretudo, fáceis de usar. A nova geração dos Certificados Digitais da Lumivex pode ser usado tanto no computador quanto no celular, smartphone e tablet. Possibilitando que você assine documentos eletrônicos, se identifique a partir de qualquer lugar de forma descomplicada ou acesse a portais do Governo (p.ex. Agência Tamboril, emissão de notas fiscais eletrônicas, processo judicial eletrônico, etc.). A Lumivex garante a autenticidade, sigilo, integridade, privacidade e total conveniência para você e para os seus negócios (sites, lojas virtuais e servidores web). "

```html
<!DOCTYPE html>
<html lang="pt-BR">
<head>
<meta charset="utf-8">
<title>Lumivex — Papel Timbrado</title>
<link rel="stylesheet" href="https://fonts.googleapis.com/css2?family=Open+Sans:wght@400;700;800&display=swap">
<style>
  :root {
    --backdrop: #ececec;
    --paper: #ffffff;
    --brand-green: #1f8f2e;
    --brand-blue: #1f2f8f;
    --brand-yellow: #f4d11a;
    --text-body: #5a5a5a;
    --text-contact: #333333;
  }
  html, body {
    margin: 0;
    padding: 0;
    width: 1200px;
    height: 1200px;
    overflow: hidden;
    background: var(--backdrop);
  }
  .canvas {
    position: relative;
    width: 1200px;
    height: 1200px;
  }
  .letterhead {
    position: absolute;
    left: 250px;
    top: 105px;
    width: 700px;
    height: 990px;
    background: var(--paper);
    overflow: hidden;
    font-family: "Open Sans", Arial, sans-serif;
  }
  .brand {
    position: absolute;
    top: 52px;
    left: 0;
    width: 100%;
    text-align: center;
  }
  .brand-lockup {
    display: inline-flex;
    align-items: center;
    gap: 12px;
  }
  .brand-mark {
    width: 26px;
    height: 26px;
    background: var(--brand-green);
  }
  .brand-name {
    font-weight: 800;
    font-size: 44px;
    letter-spacing: 1px;
    color: var(--brand-blue);
    line-height: 1;
  }
  .brand-tagline {
    margin-top: 6px;
    font-size: 10px;
    font-weight: 700;
    letter-spacing: 4px;
    color: var(--brand-green);
  }
  .body-copy {
    position: absolute;
    top: 290px;
    left: 57px;
    width: 508px;
    font-size: 12.5px;
    line-height: 18px;
    color: var(--text-body);
    text-align: justify;
  }
  .body-copy p {
    margin: 0 0 18px;
  }
  .accent-area {
    position: absolute;
    left: 420px;
    top: 730px;
    width: 280px;
    height: 260px;
    background: linear-gradient(160deg, var(--brand-green) 0%, var(--brand-green) 40%, var(--brand-blue) 75%, var(--brand-yellow) 100%);
  }
  .contact-list {
    position: absolute;
    left: 58px;
    top: 892px;
    margin: 0;
    padding: 0;
    list-style: none;
    font-size: 13px;
    color: var(--text-contact);
  }
  .contact-item {
    display: flex;
    align-items: center;
    gap: 8px;
    height: 21px;
  }
  .contact-item.phones {
    font-weight: 700;
    font-size: 16px;
    height: 26px;
  }
  .contact-icon {
    width: 14px;
    height: 14px;
    fill: var(--text-contact);
    flex: none;
  }
  .phone-gap {
    width: 12px;
  }
</style>
</head>
<body>
<main class="canvas">
  <article class="letterhead">
    <header class="brand">
      <div class="brand-lockup">
        <span class="brand-mark"></span>
        <span class="brand-name">LUMIVEX</span>
      </div>
      <div class="brand-tagline">CERTIFICAÇÃO DIGITAL</div>
    </header>

    <section class="body-copy">
      <p>Lorem ipsum dolor sit amet, consectetur adipiscing elit. Fusce eu lorem convallis odio commodo aliquet vitae in dolor. Vivamus euismod id ipsum at laoreet. Cras nec velit placerat, efficitur arcu et, porta dolor. Mauris ornare pellentesque lobortis. Praesent et cursus libero. Maecenas ut tellus lacinia, semper turpis eget, molestie sem. Pellentesque at tortor vitae velit porta tristique. Nulla suscipit dui pulvinar sem auctor varius. Sed vitae metus vel dolor rhoncus faucibus. Maecenas vel pulvinar quam.</p>
      <p>Sed faucibus nisl ut leo viverra accumsan quis et massa. Nam eleifend maximus ligula ut condimentum. Donec a nunc ut ante placerat auctor. Pellentesque in sem ultrices erat vehicula ullamcorper. Nulla ac porttitor ante, eu sagittis diam. Vivamus ut molestie magna. Morbi commodo molestie mattis. Donec maximus sodales risus a laoreet. Integer id finibus nisl. Morbi sed purus euismod, convallis nunc at, bibendum dui. Nunc risus leo, tempus nec mi vitae, congue ullamcorper magna. Vestibulum tellus metus, mollis sit amet tortor vitae, semper sollicitudin sem.</p>
      <p>Praesent non purus quis elit fermentum posuere. Vestibulum mollis aliquet nunc, eleifend fermentum dolor imperdiet sed. Aenean diam magna, iaculis a mattis vel, viverra at orci. Aliquam eget ultricies ipsum. Etiam arcu neque, lacinia ac augue non, feugiat consequat urna. Maecenas at massa est. Etiam eu enim congue, molestie ante vel, gravida tortor. Maecenas tempus dui in convallis consequat. Quisque facilisis, mauris non convallis placerat, urna mauris viverra erat, at condimentum felis erat eu purus.</p>
    </section>

    <div class="accent-area" role="img" aria-label="Área decorativa com faixas nas cores verde, azul e amarelo"></div>

    <ul class="contact-list">
      <li class="contact-item phones">
        <svg class="contact-icon" viewBox="0 0 24 24"><path d="M6.6 10.8a15.1 15.1 0 0 0 6.6 6.6l2.2-2.2a1 1 0 0 1 1-.25 11.4 11.4 0 0 0 3.6.57 1 1 0 0 1 1 1V20a1 1 0 0 1-1 1A17 17 0 0 1 3 4a1 1 0 0 1 1-1h3.5a1 1 0 0 1 1 1c0 1.25.2 2.45.57 3.57a1 1 0 0 1-.25 1z"/></svg>
        <span>(00) 0000-0000</span>
        <span class="phone-gap"></span>
        <svg class="contact-icon" viewBox="0 0 24 24"><path d="M7 1h10a2 2 0 0 1 2 2v18a2 2 0 0 1-2 2H7a2 2 0 0 1-2-2V3a2 2 0 0 1 2-2zm0 3v14h10V4zm5 15.5a1 1 0 1 0 0 2 1 1 0 0 0 0-2z"/></svg>
        <span>(00) 90000-0000</span>
      </li>
      <li class="contact-item">
        <svg class="contact-icon" viewBox="0 0 24 24"><path d="M2 5h20v14H2zm2 2v.5l8 5 8-5V7zm0 2.9V17h16V9.9l-8 5z"/></svg>
        <span>contato@lumivex.com.br</span>
      </li>
      <li class="contact-item">
        <svg class="contact-icon" viewBox="0 0 24 24"><path d="M12 2a10 10 0 1 0 0 20 10 10 0 0 0 0-20zm6.9 6h-2.9a15.6 15.6 0 0 0-1.4-3.6A8 8 0 0 1 18.9 8zM12 4c.8 1.2 1.5 2.5 1.9 4h-3.8c.4-1.5 1.1-2.8 1.9-4zM4.3 14a8.2 8.2 0 0 1 0-4h3.4a16 16 0 0 0 0 4zm.8 2h2.9c.3 1.3.8 2.5 1.4 3.6A8 8 0 0 1 5.1 16zM8 8H5.1a8 8 0 0 1 4.3-3.6C8.8 5.5 8.300 6.7 8 8zm4 12c-.8-1.2-1.5-2.5-1.9-4h3.8c-.4 1.5-1.1 2.8-1.9 4zm2.3-6H9.7a14.7 14.7 0 0 1 0-4h4.6a14.7 14.7 0 0 1 0 4zm.3 5.6c.6-1.1 1.1-2.3 1.4-3.6h2.9a8 8 0 0 1-4.3 3.6zm1.7-5.6a16 16 0 0 0 0-4h3.4a8.2 8.2 0 0 1 0 4z"/></svg>
        <span>www.lumivex.com.br</span>
      </li>
    </ul>
  </article>
</main>
</body>
</html>
```